STI/STD Medical Clinic- Wellspring Crest Partners, Inc Website

We are a Wellspring Crest in florida looking for a website. We want to be professional but also playful. We want a buildout similar to the website listed below as our clinic is very similar to theirs.

This is a great example of a clinic doing similar stuff as us. We obviously do not want their color scheme but their format and buildout work. Please see our logo attached for color schemes etc.

https://bluefernclinicmiami.org

Industry/Entity Type

Medical

Coding

Coded - Design and coding required

Number of Pages Required

5+ page

Font styles to use
Sans Serif

```html
<!DOCTYPE html>
<html lang="en">
<head>
<meta charset="utf-8">
<title>Wellspring Crest Partners — Home</title>
<link href="https://fonts.googleapis.com/css2?family=Poppins:wght@400;500;600&family=Roboto:wght@300;400;500&display=swap" rel="stylesheet">
<style>
  :root {
    --brand-blue: #1f74e0;
    --brand-navy: #0f2a55;
    --accent-sky: #4aa3ff;
    --white: #ffffff;
    --ink: #1d2433;
    --hero-top: #6f8596;
    --hero-mid: #8a9aa6;
    --hero-low: #4d5d6b;
  }
  * { box-sizing: border-box; margin: 0; padding: 0; }
  html, body { width: 1200px; height: 675px; overflow: hidden; background: var(--white); }
  body { font-family: "Poppins", sans-serif; color: var(--ink); }

  .top-bar {
    height: 48px; background: var(--brand-blue); color: var(--white);
    display: flex; align-items: center; padding: 0 40px; font-size: 14px; font-weight: 500;
  }
  .top-bar .contact { display: flex; align-items: center; gap: 10px; }
  .top-bar .hours { margin-left: 120px; display: flex; align-items: center; gap: 10px; }
  .top-bar .social { margin-left: auto; display: flex; gap: 18px; }
  .social span { width: 14px; height: 14px; border-radius: 50%; background: var(--white); display: block; }

  .site-nav {
    height: 78px; display: flex; align-items: center; padding: 0 40px; background: var(--white);
  }
  .brand { display: flex; align-items: center; gap: 10px; font-weight: 600; font-size: 20px; color: var(--brand-navy); }
  .brand .mark { width: 26px; height: 26px; border-radius: 50%; background: var(--brand-blue); }
  .menu { display: flex; gap: 44px; margin-left: 110px; font-size: 15px; font-weight: 500; }
  .menu a { text-decoration: none; color: var(--ink); }
  .menu a.active { color: var(--brand-blue); }
  .donate {
    margin-left: auto; display: flex; align-items: center; gap: 10px;
    border: 1px solid #d6dbe3; padding: 11px 26px; font-size: 15px; font-weight: 500; color: var(--ink);
  }

  .hero {
    position: relative; height: 549px;
    display: flex; flex-direction: column; align-items: center; justify-content: center;
    color: var(--white); text-align: center;
  }
  .hero-photo {
    position: absolute; inset: 0;
    background: linear-gradient(180deg, var(--hero-top) 0%, var(--hero-mid) 45%, var(--hero-low) 100%);
  }
  .hero-content { position: relative; margin-top: -40px; }
  .hero .welcome { font-family: "Roboto", sans-serif; font-weight: 400; font-size: 34px; margin-bottom: 22px; }
  .hero h1 { font-family: "Roboto", sans-serif; font-weight: 300; font-size: 58px; letter-spacing: 1px; }
  .hero h1 .accent { color: var(--accent-sky); font-weight: 500; }
  .cta { display: flex; gap: 22px; justify-content: center; margin-top: 34px; }
  .btn {
    display: flex; align-items: center; gap: 12px; padding: 14px 30px;
    font-size: 15px; font-weight: 500; color: var(--white);
  }
  .btn.primary { background: var(--brand-blue); }
  .btn.secondary { background: var(--brand-navy); }
</style>
</head>
<body>
  <header>
    <div class="top-bar">
      <div class="contact">
        <svg width="18" height="18" viewBox="0 0 18 18"><rect x="1" y="3" width="16" height="12" rx="1.5" fill="#fff"/><path d="M2 4.5l7 5 7-5" stroke="#1f74e0" stroke-width="1.6" fill="none"/></svg>
        hello@wellspringcrest.org
      </div>
      <div class="hours">
        <svg width="18" height="18" viewBox="0 0 18 18"><circle cx="9" cy="9" r="8" fill="none" stroke="#fff" stroke-width="2"/><path d="M9 5v4l3 2" stroke="#fff" stroke-width="2" fill="none"/></svg>
        Mon - Sat: 9.00 am - 6.00 pm
      </div>
      <div class="social" aria-label="Social links">
        <span></span><span></span><span></span><span></span>
      </div>
    </div>
    <nav class="site-nav">
      <div class="brand"><span class="mark"></span>Wellspring Crest</div>
      <div class="menu">
        <a class="active" href="#">Home</a>
        <a href="#">About</a>
        <a href="#">Services</a>
        <a href="#">News</a>
      </div>
      <div class="donate">
        <svg width="16" height="16" viewBox="0 0 16 16"><rect x="2" y="6" width="12" height="9" fill="#1d2433"/><path d="M5 6V4a3 3 0 0 1 6 0v2" stroke="#1d2433" stroke-width="2" fill="none"/></svg>
        Donate
      </div>
    </nav>
  </header>

  <section class="hero">
    <div class="hero-photo" role="img" aria-label="Photo of a team of doctors and nurses in white coats"></div>
    <div class="hero-content">
      <p class="welcome">Welcome to Wellspring Crest</p>
      <h1>HEALTHCARE <span class="accent">&amp; CLINIC</span></h1>
      <div class="cta">
        <div class="btn primary">
          <svg width="16" height="16" viewBox="0 0 16 16"><rect x="1" y="3" width="14" height="12" fill="none" stroke="#fff" stroke-width="2"/><path d="M1 7h14M5 1v4M11 1v4" stroke="#fff" stroke-width="2"/></svg>
          Appointment
        </div>
        <div class="btn secondary">
          <svg width="16" height="16" viewBox="0 0 16 16"><circle cx="8" cy="8" r="7" fill="none" stroke="#fff" stroke-width="2"/><path d="M7 5l3 3-3 3" stroke="#fff" stroke-width="2" fill="none"/></svg>
          Consultation
        </div>
      </div>
    </div>
  </section>
</body>
</html>
```